Employment Agency Website Design

We are working with an employment agency in California.

Some sites to use for content/competitors and inspiration:

https://www.dovelanejobs.example/us/en
https://www.perimowork.example
https://www.tamberlinehire.example
https://www.vintrastaff.example/en
https://www.olmirajobs.example
https://www.quarnstaffing.example

Thank you for taking the time to consider designing a website for us. We are web developers based in Stockton, CA, USA. Most of our projects go through the same process. Understanding this process may help you win a project with us. We custom-code all of our websites in-house. We don’t have any requirements as to what tools you use for your design, but we prefer Figma files. For any design that we label as four-stars, we send it to the client for review. The client picks the final design they want us to use. Once we complete this process, we will continue to show additional clients all the four-star sites and purchase them later. Your designs will have multiple chances to sell. For better chances of success, we ask that you follow these guidelines.

IMAGES:
If you use any images or icons in the design, we ask that you have a link to the asset so we can purchase the image/icon. Most of the designs we submit do not have the customer’s images on them unless they have some great images. Be creative; show us the feeling you are trying to portray with your image choices. Use any royalty-free site you choose. We subscribe to Velsor and mainly use their images, but we can purchase images outside of Velsor. PLEASE NOTE: we will not submit designs to clients with watermarks on the images.

FONTS:
We ask that you identify the fonts used in the design. This can be done in a message if you want. We typically use Google Fonts and Velsor Fonts.

CONTENT:
We're always open to different content and ideas. We often submit designs with stock images so the client can see our vision. We typically take pictures after the website launch to use their images with our vision. Lorem Ipsum is fine for paragraphs, but we ask that you write the headers in correct English. We want to be able to show the vision and identify the sections of the website.

INSPIRATION:
We typically add a couple of links in the brief of websites we like to help you get started in your design.

REVISIONS:
We do not often ask for revisions of the designs unless we see something in the design that may not appeal to the client. If there are slight changes that we want to make, we do that in the development process.

FEEDBACK:
We rarely give feedback on designs during the design process. We are working on many website projects and do not have the time to provide feedback. We usually respond if your request is well thought out and asks specific questions, but a note asking “feedback, please” usually goes unanswered.

```html
<!DOCTYPE html>
<html lang="en">
<head>
<meta charset="utf-8">
<title>Brightpath Talent — Find a job and unlock your potential</title>
<link href="https://fonts.googleapis.com/css2?family=Lato:wght@300;400;700;900&display=swap" rel="stylesheet">
<style>
:root{
  --red:#c01d2e;
  --ink:#151515;
  --text:#2a2a2a;
  --muted:#6d6d6d;
  --grey:#efefef;
  --white:#ffffff;
}
*{box-sizing:border-box;margin:0;padding:0}
html,body{width:1200px;height:3399px;overflow:hidden}
body{font-family:'Lato',sans-serif;color:var(--text);background:var(--white);position:relative}
.accent{color:var(--red)}
.rule{position:absolute;width:56px;height:4px;background:var(--ink)}
h2.title{font-weight:900;font-size:41px;line-height:56px;color:var(--ink);letter-spacing:-0.3px}
p.body{font-size:16px;line-height:29px;color:var(--text);text-align:justify}
.link{font-size:20px;color:var(--red);display:flex;align-items:center;gap:10px;text-decoration:none}
.link svg{width:20px;height:14px}

/* header */
.site-header{position:absolute;left:0;top:0;width:1200px;height:86px}
.brand{position:absolute;left:104px;top:28px;display:flex;align-items:center;gap:8px}
.brand-mark{width:24px;height:24px;border-radius:50%;background:var(--red);display:block}
.brand-name{font-size:17px;font-weight:700;color:var(--ink);white-space:nowrap}
.nav{position:absolute;left:299px;top:34px;display:flex;gap:22px;font-size:13px;color:var(--ink)}
.nav span{display:flex;align-items:center;gap:10px}
.nav svg{width:11px;height:7px}
.search-ico{position:absolute;left:923px;top:33px;width:18px;height:18px}
.btn-start{position:absolute;left:964px;top:22px;width:136px;height:41px;border-radius:21px;background:var(--red);color:var(--white);font-size:13px;display:flex;align-items:center;justify-content:center}

/* hero */
.hero{position:absolute;left:100px;top:87px;width:1000px;height:458px;border-radius:16px;overflow:hidden;background:linear-gradient(115deg,#242424 0%,#0d0d0d 45%,#2b2b2b 70%,#111 100%)}
.hero h1{position:absolute;left:68px;top:80px;font-size:55px;line-height:63px;font-weight:700;color:var(--white);letter-spacing:-0.5px}
.hero .lead{position:absolute;left:68px;top:216px;width:520px;font-size:26px;line-height:38px;font-weight:300;color:var(--white)}
.hero-photo{position:absolute;left:610px;top:30px;width:360px;height:428px;border-radius:180px 180px 0 0;background:linear-gradient(180deg,#5a5a5a,#3a3a3a 60%,#d8d8d8)}
.jobsearch{position:absolute;left:68px;top:316px;width:497px;height:63px;background:var(--white);border-radius:3px}
.field{position:absolute;top:15px}
.field small{display:block;font-size:9px;color:var(--red)}
.field span{display:flex;align-items:center;gap:20px;font-size:13px;color:var(--ink);margin-top:5px}
.field svg{width:11px;height:7px}
.jobsearch .go{position:absolute;right:7px;top:7px;width:48px;height:48px;background:var(--red);border-radius:2px;display:flex;align-items:center;justify-content:center}

/* why */
.why-text{position:absolute;left:100px;top:630px;width:440px}
.features{position:absolute;left:597px;top:612px;width:503px}
.feature{display:flex;gap:22px;height:97px}
.feature .ico{flex:0 0 70px;height:70px;border-radius:50%;background:var(--red);display:flex;align-items:center;justify-content:center}
.feature .ico svg{width:30px;height:30px}
.feature h3{font-size:20px;font-weight:700;color:var(--ink);margin-top:3px}
.feature p{font-size:16px;line-height:25px;text-align:justify;margin-top:2px}
.person-photo{position:absolute;left:100px;top:960px;width:445px;height:472px;background:radial-gradient(ellipse at 50% 45%,#cfcfcf,#f3f3f3 70%)}
.meet{position:absolute;left:597px;top:1066px;width:503px}

/* categories */
.categories{position:absolute;left:0;top:1432px;width:1200px;height:786px;background:var(--grey)}
.categories .head{position:absolute;left:0;top:80px;width:1200px;text-align:center}
.categories .head p{font-size:16px;line-height:29px;color:var(--text);margin-top:10px}
.card{position:absolute;width:234px;height:197px;background:var(--white);border-radius:10px;text-align:center}
.card svg{position:absolute;left:82px;top:38px;width:70px;height:70px}
.card span{position:absolute;left:0;top:127px;width:100%;font-size:16px;line-height:20px;color:var(--ink)}
.btn-more{position:absolute;left:529px;top:685px;width:143px;height:44px;border-radius:22px;background:var(--red);color:var(--white);font-size:16px;display:flex;align-items:center;justify-content:center}

/* talent */
.talent-text{position:absolute;left:100px;top:2296px;width:440px}
.team-photo{position:absolute;left:597px;top:2277px;width:503px;height:354px;border-radius:12px;background:linear-gradient(135deg,#6b625a,#2c2824 60%,#141210)}

/* testimonial */
.quote{position:absolute;left:100px;top:2690px;width:1000px;height:310px;border-radius:16px;background:var(--red);color:var(--white)}
.quote .mark{position:absolute;font-size:180px;font-weight:900;color:rgba(0,0,0,0.12);line-height:1}
.quote blockquote{position:absolute;left:123px;top:68px;width:755px;font-size:20px;line-height:28px;text-align:justify}
.quote cite{position:absolute;left:123px;top:214px;font-style:normal;font-size:20px;font-weight:700}
.stars{position:absolute;left:123px;top:244px;display:flex;gap:5px}
.stars svg{width:17px;height:17px}
.arrows{position:absolute;left:790px;top:220px;display:flex;gap:22px}
.arrows svg{width:32px;height:20px}

/* footer */
.site-footer{position:absolute;left:0;top:3057px;width:1200px;height:342px;background:var(--grey)}
.foot-brand{position:absolute;left:100px;top:70px;display:flex;flex-direction:column;align-items:flex-start;gap:8px}
.foot-brand .brand-mark{width:36px;height:36px}
.foot-brand .brand-name{font-size:14px}
.foot-about{position:absolute;left:100px;top:150px;width:285px;font-size:12px;line-height:18px;text-align:justify}
.socials{position:absolute;left:100px;top:234px;display:flex;gap:10px}
.socials i{width:25px;height:25px;border-radius:50%;background:var(--red);display:block}
.col{position:absolute;font-size:12px;line-height:23px;color:var(--ink)}
.col h4{font-size:12px;font-weight:700;margin-bottom:6px}
.ask{position:absolute;left:852px;top:68px;width:248px}
.ask h4{font-size:16px;font-weight:700;color:var(--ink);margin-bottom:14px}
.ask .input{height:34px;background:var(--white);border:1px solid #e2e2e2;font-size:11px;color:#b5b5b5;padding:10px 14px;margin-bottom:10px}
.ask .send{width:100px;height:32px;background:var(--red);color:var(--white);font-size:14px;display:flex;align-items:center;justify-content:center}
.foot-line{position:absolute;left:100px;top:272px;width:1000px;height:1px;background:#cfcfcf}
.copyright{position:absolute;left:0;top:292px;width:1200px;text-align:center;font-size:10px;color:#8a8a8a}
</style>
</head>
<body>

<header class="site-header">
  <div class="brand"><i class="brand-mark"></i><span class="brand-name">Brightpath Talent</span></div>
  <nav class="nav">
    <span>FIND JOBS <svg viewBox="0 0 11 7"><path d="M1 1l4.5 4.5L10 1" fill="none" stroke="#151515" stroke-width="1.5"/></svg></span>
    <span>HIRE TALENT <svg viewBox="0 0 11 7"><path d="M1 1l4.5 4.5L10 1" fill="none" stroke="#151515" stroke-width="1.5"/></svg></span>
    <span>INSIGHTS</span><span>BLOG</span><span>ABOUT</span><span>SUPPORT</span>
  </nav>
  <svg class="search-ico" viewBox="0 0 18 18"><circle cx="7.5" cy="7.5" r="6" fill="none" stroke="#151515" stroke-width="2"/><path d="M12 12l5 5" stroke="#151515" stroke-width="2"/></svg>
  <div class="btn-start">GET STARTED</div>
</header>

<section class="hero">
  <h1>Find a job and unlock<br>your <span class="accent">potential</span></h1>
  <p class="lead">Connecting talent with opportunities for a brighter career journey</p>
  <div class="jobsearch">
    <div class="field" style="left:15px"><small>Job Title</small><span>UI/UX Designer <svg viewBox="0 0 11 7"><path d="M1 1l4.5 4.5L10 1" fill="none" stroke="#151515" stroke-width="1.5"/></svg></span></div>
    <div class="field" style="left:158px"><small>Location</small><span>California, US <svg viewBox="0 0 11 7"><path d="M1 1l4.5 4.5L10 1" fill="none" stroke="#151515" stroke-width="1.5"/></svg></span></div>
    <div class="field" style="left:301px"><small>Type</small><span>Fulltime/WFO <svg viewBox="0 0 11 7"><path d="M1 1l4.5 4.5L10 1" fill="none" stroke="#151515" stroke-width="1.5"/></svg></span></div>
    <div class="go"><svg width="18" height="18" viewBox="0 0 18 18"><circle cx="7.5" cy="7.5" r="5.5" fill="none" stroke="#fff" stroke-width="2"/><path d="M11.5 11.5l5 5" stroke="#fff" stroke-width="2"/></svg></div>
  </div>
  <div class="hero-photo" role="img" aria-label="Photo of a smiling professional woman in a light blazer and striped top, hands on hips"></div>
</section>

<div class="rule" style="left:100px;top:608px"></div>
<section class="why-text">
  <h2 class="title">What Makes Brightpath<br>Talent the <span class="accent">Best</span> Choice?</h2>
  <p class="body" style="margin-top:30px">Discover extensive opportunities with advanced matching and personalized insights. Brightpath Talent stands out as the ultimate choice for job seekers.</p>
  <a class="link" style="margin-top:46px">See More Information <svg viewBox="0 0 20 14"><path d="M0 7h18M12 1l6 6-6 6" fill="none" stroke="#c01d2e" stroke-width="1.6"/></svg></a>
</section>

<section class="features">
  <div class="feature"><div class="ico"><svg viewBox="0 0 30 30" fill="none" stroke="#fff" stroke-width="1.6"><circle cx="15" cy="10" r="5"/><path d="M5 26c0-6 4-9 10-9s10 3 10 9z"/></svg></div><div><h3>Personalized Matches</h3><p>Tailored job recommendations based on your skills and preferences for a perfect career fit.</p></div></div>
  <div class="feature"><div class="ico"><svg viewBox="0 0 30 30" fill="none" stroke="#fff" stroke-width="1.6"><rect x="4" y="9" width="22" height="15" rx="2"/><path d="M11 9V6h8v3M4 15h22"/></svg></div><div><h3>Extensive Opportunities</h3><p>Access a wide array of job listings across industries, ensuring diverse and plentiful options.</p></div></div>
  <div class="feature"><div class="ico"><svg viewBox="0 0 30 30" fill="none" stroke="#fff" stroke-width="1.6"><path d="M4 26h22M7 26V17M13 26V13M19 26V15M25 26V9M6 12l7-5 5 4 7-6"/></svg></div><div><h3>Career Growth Focus</h3><p>Prioritizing professional growth with resources for ongoing career development.</p></div></div>
  <div class="feature"><div class="ico"><svg viewBox="0 0 30 30" fill="none" stroke="#fff" stroke-width="1.6"><circle cx="15" cy="12" r="7"/><path d="M12 12l2 2 4-4M11 18l-2 9 6-3 6 3-2-9"/></svg></div><div><h3>Trustworthy Network</h3><p>Join a trusted community for transparent connections between employers and job seekers, built on integrity.</p></div></div>
</section>

<div class="person-photo" role="img" aria-label="Photo of a smiling professional woman in a light blazer pointing upward"></div>

<div class="rule" style="left:597px;top:1044px"></div>
<section class="meet">
  <h2 class="title">Meet Us, Your <span class="accent">Trusted</span><br>Talent Acquisition Partner</h2>
  <p class="body" style="margin-top:22px">With a commitment to transparency and integrity, we connect employers with exceptional candidates, fostering success in every partnership. Explore our story and discover why we stand out as your trusted choice for building a skilled and motivated workforce.</p>
  <a class="link" style="margin-top:46px">Learn More <svg viewBox="0 0 20 14"><path d="M0 7h18M12 1l6 6-6 6" fill="none" stroke="#c01d2e" stroke-width="1.6"/></svg></a>
</section>

<section class="categories">
  <div class="rule" style="left:572px;top:55px"></div>
  <div class="head">
    <h2 class="title">Explore Our Job <span class="accent">Categories</span></h2>
    <p>Explore diverse job categories tailored to your career aspirations. Navigate your<br>professional journey with our wide range of opportunities.</p>
  </div>
  <div class="card" style="left:100px;top:224px"><svg viewBox="0 0 70 70" fill="none" stroke="#c01d2e" stroke-width="3"><circle cx="32" cy="32" r="27"/><path d="M5 32h54M32 5c-10 10-10 44 0 54M32 5c10 10 10 44 0 54M48 50l-5 5 5 5M58 50l5 5-5 5"/></svg><span>INFORMATION AND<br>TECHNOLOGY</span></div>
  <div class="card" style="left:355px;top:224px"><svg viewBox="0 0 70 70" fill="none" stroke="#c01d2e" stroke-width="3"><path d="M35 62C10 44 4 32 4 22 4 12 12 5 21 5c6 0 11 3 14 8 3-5 8-8 14-8 9 0 17 7 17 17 0 10-6 22-31 40z"/><path d="M8 34h14l5-10 7 18 6-12h22"/></svg><span>HEALTHCARE AND<br>WELLNESS</span></div>
  <div class="card" style="left:610px;top:224px"><svg viewBox="0 0 70 70" fill="none" stroke="#c01d2e" stroke-width="3"><ellipse cx="48" cy="10" rx="16" ry="6"/><path d="M32 10v36c0 3 7 6 16 6s16-3 16-6V10M32 22c0 3 7 6 16 6s16-3 16-6M32 34c0 3 7 6 16 6s16-3 16-6"/><path d="M4 40c0-3 9-6 20-6M4 40v14c0 4 12 8 28 8M4 47c0 4 12 7 28 7"/></svg><span>FINANCE AND<br>ACCOUNTING</span></div>
  <div class="card" style="left:866px;top:224px"><svg viewBox="0 0 70 70" fill="none" stroke="#c01d2e" stroke-width="3"><path d="M35 5C18 5 5 18 5 34s13 30 28 30c5 0 6-5 3-8-3-4 0-9 5-9h9c8 0 14-6 14-13C64 17 51 5 35 5z"/><circle cx="20" cy="30" r="4"/><circle cx="28" cy="17" r="4"/><circle cx="42" cy="16" r="4"/><circle cx="52" cy="27" r="4"/></svg><span>CREATIVE ARTS AND<br>DESIGN</span></div>
  <div class="card" style="left:100px;top:443px"><svg viewBox="0 0 70 70" fill="none" stroke="#c01d2e" stroke-width="3"><path d="M6 28h12l30-16v44L18 42H6zM18 28v14M12 42l5 16h8l-4-16"/><rect x="48" y="12" width="10" height="44" rx="3"/></svg><span>SALES AND<br>MARKETING</span></div>
  <div class="card" style="left:355px;top:443px"><svg viewBox="0 0 70 70" fill="none" stroke="#c01d2e" stroke-width="3"><path d="M24 18a11 11 0 0 1 22 0zM22 18h26M26 22a9 9 0 0 0 18 0"/><path d="M8 62c0-14 11-22 27-22s27 8 27 22z"/><path d="M32 6h6"/></svg><span>ENGINEERING AND<br>MANUFACTURING</span></div>
  <div class="card" style="left:610px;top:443px"><svg viewBox="0 0 70 70" fill="none" stroke="#c01d2e" stroke-width="3"><path d="M4 24L36 10l30 14-30 14z"/><path d="M18 30v16c8 6 28 6 36 0V30M10 26v18l-4 12h8l-4-12"/></svg><span>EDUCATION AND<br>TRAINING</span></div>
  <div class="card" style="left:866px;top:443px"><svg viewBox="0 0 70 70" fill="none" stroke="#c01d2e" stroke-width="3"><circle cx="26" cy="18" r="11"/><path d="M4 56c0-13 9-20 22-20 5 0 9 1 12 3M4 56h30"/><path d="M44 38l20 20M48 34a8 8 0 1 0 4 4l-6 2z"/></svg><span>HOSPITALITY AND<br>SERVICE INDUSTRY</span></div>
  <div class="btn-more">FIND MORE</div>
</section>

<div class="rule" style="left:100px;top:2273px"></div>
<section class="talent-text">
  <h2 class="title">Find the Right Talent to<br><span class="accent">Elevate</span> Your Work</h2>
  <p class="body" style="margin-top:22px">Unlock success by finding the perfect talent to complement your team. Explore our curated pool of skilled professionals ready to contribute expertise and innovation to your projects. Elevate your work with the right talent at your fingertips.</p>
  <a class="link" style="margin-top:46px">Hire New Talent <svg viewBox="0 0 20 14"><path d="M0 7h18M12 1l6 6-6 6" fill="none" stroke="#c01d2e" stroke-width="1.6"/></svg></a>
</section>
<div class="team-photo" role="img" aria-label="Photo of a team meeting around a long table in a warm, modern office"></div>

<section class="quote">
  <div class="mark" style="left:92px;top:20px">“</div>
  <div class="mark" style="left:820px;top:90px">”</div>
  <blockquote>Working with Brightpath Talent has been a game-changer for my hiring process. Their dedicated team understood our unique needs, ensuring they found the perfect candidates swiftly. The quality of talent they provided significantly elevated our team, making them our go-to partner for all recruitment needs.</blockquote>
  <cite>Marisol Dunhaven</cite>
  <div class="stars">
    <svg viewBox="0 0 20 20"><path d="M10 1l2.6 6.2 6.7.5-5.1 4.4 1.6 6.6L10 15.2 4.2 18.7l1.6-6.6L.7 7.7l6.7-.5z" fill="#fff"/></svg>
    <svg viewBox="0 0 20 20"><path d="M10 1l2.6 6.2 6.7.5-5.1 4.4 1.6 6.6L10 15.2 4.2 18.7l1.6-6.6L.7 7.7l6.7-.5z" fill="#fff"/></svg>
    <svg viewBox="0 0 20 20"><path d="M10 1l2.6 6.2 6.7.5-5.1 4.4 1.6 6.6L10 15.2 4.2 18.7l1.6-6.6L.7 7.7l6.7-.5z" fill="#fff"/></svg>
    <svg viewBox="0 0 20 20"><path d="M10 1l2.6 6.2 6.7.5-5.1 4.4 1.6 6.6L10 15.2 4.2 18.7l1.6-6.6L.7 7.7l6.7-.5z" fill="#fff"/></svg>
    <svg viewBox="0 0 20 20"><path d="M10 1l2.6 6.2 6.7.5-5.1 4.4 1.6 6.6L10 15.2 4.2 18.7l1.6-6.6L.7 7.7l6.7-.5z" fill="#fff"/></svg>
  </div>
  <div class="arrows">
    <svg viewBox="0 0 32 20"><path d="M32 10H2M10 2L2 10l8 8" fill="none" stroke="rgba(0,0,0,0.3)" stroke-width="1.8"/></svg>
    <svg viewBox="0 0 32 20"><path d="M0 10h30M22 2l8 8-8 8" fill="none" stroke="#fff" stroke-width="1.8"/></svg>
  </div>
</section>

<footer class="site-footer">
  <div class="foot-brand"><i class="brand-mark"></i><span class="brand-name">Brightpath Talent</span></div>
  <p class="foot-about">We're your gateway to unparalleled opportunities, offering advanced matching and personalized insights for a transformative career journey.</p>
  <div class="socials"><i></i><i></i><i></i></div>
  <div class="col" style="left:470px;top:68px"><h4>Contact Us</h4>hello@brightpathtalent.example<br>California United States<br>(555) 010 - 2244
    <h4 style="margin-top:16px">Company</h4>Contact Us<br>FAQ</div>
  <div class="col" style="left:696px;top:68px"><h4>Quick Links</h4>Find Jobs<br>Hire Talent<br>Insights<br>Blog<br>About Us<br>Support</div>
  <div class="ask"><h4>Ask Me Below</h4><div class="input">Write your email</div><div class="input">Write your question or comment</div><div class="send">Send</div></div>
  <div class="foot-line"></div>
  <div class="copyright">© 2024 Brightpath Talent | Privacy Policy | Term &amp; Conditions</div>
</footer>

</body>
</html>
```